Birchford Realty Business Card

Business Card:

Somewhere on front of card, please include Broker License Number: 5839162

Website is BirchfordRealty.example

Address is:
7218 Crestover Ave E
Maplecrest, MI 48271

I'll let you use creative freedom on the rest; we obviously need Name, Title, Email (@BirchfordRealty.example), Office Phone, Cell Phone.

Don't want any special die-cutting, just a standard size business card.

On the back, include a place for the date and time of an appointment to be written in pen.

Requirements
Must have
• Our logo, attached to email.

```html
<!DOCTYPE html>
<html lang="en">
<head>
<meta charset="UTF-8">
<title>Birchford Realty Business Card</title>
<link href="https://fonts.googleapis.com/css2?family=Fira+Sans:wght@300;400;600&display=swap" rel="stylesheet">
<style>
  :root {
    --backdrop: #ebebeb;
    --card: #f4f4f4;
    --navy: #2b2a74;
    --ink: #555555;
    --muted: #9a9a9a;
    --field: #ffffff;
    --label: #c9c9e0;
    --heading: #6b6b6b;
  }
  * { box-sizing: border-box; margin: 0; padding: 0; }
  html, body {
    width: 1200px; height: 1066px; overflow: hidden;
    background: var(--backdrop);
    font-family: "Fira Sans", sans-serif;
  }
  .card {
    position: absolute; left: 330px;
    width: 540px; height: 309px;
    background: var(--card);
    box-shadow: 0 4px 14px rgba(0,0,0,0.12);
    overflow: hidden;
  }
  .card-front { top: 150px; border-bottom: 8px solid var(--navy); }
  .card-back { top: 580px; background: var(--navy); }

  .brand-name {
    position: absolute; right: 40px; top: 46px;
    font-size: 34px; font-weight: 600; color: var(--navy);
    letter-spacing: -0.5px; white-space: nowrap;
  }
  .agent { position: absolute; left: 48px; top: 100px; }
  .agent-name { font-size: 20px; font-weight: 600; color: var(--navy); }
  .agent-title { font-size: 12px; color: var(--muted); text-transform: uppercase; margin-top: 2px; }
  .contact {
    position: absolute; left: 48px; top: 166px;
    font-size: 13px; line-height: 20px; color: var(--ink);
  }
  .address {
    position: absolute; left: 48px; top: 244px;
    font-size: 13px; line-height: 20px; color: var(--ink);
  }
  .web { position: absolute; right: 36px; bottom: 50px; text-align: right; }
  .web-url { font-size: 13px; color: var(--navy); }
  .license { font-size: 10px; color: var(--muted); margin-top: 2px; }

  .back-header {
    height: 62px; background: var(--card);
    padding: 22px 36px 0;
    font-size: 17px; color: var(--heading); letter-spacing: 0.5px; text-transform: uppercase;
  }
  .field-label {
    position: absolute; font-size: 12px; color: var(--label);
    text-transform: uppercase; letter-spacing: 0.5px;
  }
  .field-box { position: absolute; background: var(--field); height: 44px; }
  .location-label { left: 44px; top: 84px; }
  .location-box { left: 44px; top: 102px; width: 452px; }
  .date-label { left: 44px; top: 172px; }
  .date-box { left: 44px; top: 190px; width: 236px; }
  .time-label { left: 300px; top: 172px; }
  .time-box { left: 300px; top: 190px; width: 196px; }
</style>
</head>
<body>
  <section class="card card-front">
    <div class="brand-name">Birchford Realty</div>
    <div class="agent">
      <div class="agent-name">Alex Carter</div>
      <div class="agent-title">Job Title</div>
    </div>
    <div class="contact">
      Phone (555) 014-2231<br>
      Cell (555) 018-7764<br>
      alex@birchfordrealty.example
    </div>
    <div class="address">
      7218 Crestover Ave E,<br>
      Maplecrest, MI 48271
    </div>
    <div class="web">
      <div class="web-url">www.birchfordrealty.example</div>
      <div class="license">Broker License Number: 5839162</div>
    </div>
  </section>

  <section class="card card-back">
    <div class="back-header">Appointment Details</div>
    <div class="field-label location-label">Location</div>
    <div class="field-box location-box"></div>
    <div class="field-label date-label">Date</div>
    <div class="field-box date-box"></div>
    <div class="field-label time-label">Time</div>
    <div class="field-box time-box"></div>
  </section>
</body>
</html>
```